Design a double sided business card

We are looking for a clean, eye-catching, and contemporary design that enhances the brand and presents a premium, professional image. Our preference is for a brown card with black gloss detailing and embossed elements; however, we are open to creative input and design suggestions that best achieve a strong visual impact.

Please see the attached existing business card for reference. We use both black and brown colours consistently across our branding.

On sample provided

```html
<!DOCTYPE html>
<html lang="en">
<head>
<meta charset="utf-8">
<title>Kestrel – Business Card</title>
<link rel="stylesheet" href="https://fonts.googleapis.com/css2?family=Poppins:wght@400;500;600;700&display=swap">
<style>
  :root {
    --page-bg: #18181b;
    --card-bg: #232427;
    --card-edge: #2c2d31;
    --sand: #cdb797;
    --silver: #c4c5c9;
    --ink: #1f1f22;
    --muted-frame: #111113;
  }
  * { box-sizing: border-box; margin: 0; padding: 0; }
  html, body {
    width: 1200px; height: 800px; overflow: hidden;
    background: var(--page-bg);
    font-family: "Poppins", sans-serif;
  }
  .canvas {
    width: 1200px; height: 800px;
    display: flex; align-items: center; justify-content: center; gap: 48px;
  }
  .card {
    position: relative;
    width: 540px; height: 318px;
    background: var(--card-bg);
    border: 1px solid var(--card-edge);
    border-radius: 26px;
    overflow: hidden;
    box-shadow: 0 18px 40px rgba(0,0,0,.45);
  }

  /* Front side */
  .card-front {
    display: flex; align-items: center; justify-content: center; gap: 26px;
  }
  .front-mark {
    width: 62px; height: 62px;
    border: 5px solid var(--muted-frame);
  }
  .front-divider {
    width: 2px; height: 92px; background: var(--muted-frame);
  }
  .front-name {
    font-size: 46px; font-weight: 600; letter-spacing: 6px;
    color: var(--silver);
  }

  /* Back side */
  .card-back .brand {
    position: absolute; left: 40px; top: 96px;
    display: flex; align-items: center; gap: 14px;
  }
  .brand-mark {
    width: 56px; height: 56px; border: 5px solid var(--sand);
  }
  .brand-name {
    font-size: 26px; font-weight: 600; letter-spacing: 3px; color: var(--sand);
  }
  .back-divider {
    position: absolute; left: 270px; top: 62px;
    width: 1.5px; height: 150px; background: var(--sand);
  }
  .contact {
    position: absolute; left: 296px; top: 56px; color: var(--sand);
  }
  .contact-name {
    font-size: 21px; font-weight: 700; letter-spacing: .5px; line-height: 1.1;
  }
  .contact-role {
    font-size: 12px; font-weight: 500; margin-bottom: 16px;
  }
  .contact-list { list-style: none; }
  .contact-list li {
    display: flex; align-items: center; gap: 9px;
    font-size: 12.5px; font-weight: 500; line-height: 1; margin-bottom: 9px;
  }
  .icon {
    width: 18px; height: 18px; border-radius: 50%;
    background: var(--sand); flex: none;
    display: flex; align-items: center; justify-content: center;
  }
  .icon svg { width: 10px; height: 10px; }
  .address-band {
    position: absolute; left: 0; right: 0; bottom: 0; height: 44px;
    background: var(--sand);
    display: flex; align-items: center; justify-content: center;
    font-size: 13px; font-weight: 500; color: var(--ink); letter-spacing: .3px;
  }
</style>
</head>
<body>
<main class="canvas">

  <section class="card card-front" aria-label="Card front">
    <div class="front-mark" aria-hidden="true"></div>
    <div class="front-divider" aria-hidden="true"></div>
    <h1 class="front-name">KESTREL</h1>
  </section>

  <section class="card card-back" aria-label="Card back">
    <div class="brand">
      <div class="brand-mark" aria-hidden="true"></div>
      <span class="brand-name">KESTREL</span>
    </div>
    <div class="back-divider" aria-hidden="true"></div>
    <div class="contact">
      <p class="contact-name">DEV ARORA</p>
      <p class="contact-role">Director</p>
      <ul class="contact-list">
        <li>
          <span class="icon"><svg viewBox="0 0 24 24"><path fill="#1f1f22" d="M6.6 10.8a15 15 0 0 0 6.6 6.6l2.2-2.2c.3-.3.7-.4 1-.2 1.1.4 2.3.6 3.6.6.6 0 1 .4 1 1V20c0 .6-.4 1-1 1A17 17 0 0 1 3 4c0-.6.4-1 1-1h3.5c.6 0 1 .4 1 1 0 1.3.2 2.5.6 3.6.1.3 0 .7-.2 1z"/></svg></span>
          0800 000 4521
        </li>
        <li>
          <span class="icon"><svg viewBox="0 0 24 24"><rect x="6" y="2" width="12" height="20" rx="2" fill="none" stroke="#1f1f22" stroke-width="2.5"/><circle cx="12" cy="18" r="1.5" fill="#1f1f22"/></svg></span>
          07700 900318
        </li>
        <li>
          <span class="icon"><svg viewBox="0 0 24 24"><rect x="2" y="5" width="20" height="14" rx="1" fill="#1f1f22"/><path d="M3 6l9 7 9-7" fill="none" stroke="#cdb797" stroke-width="2"/></svg></span>
          dev@kestrelhome.co.uk
        </li>
        <li>
          <span class="icon"><svg viewBox="0 0 24 24"><g fill="none" stroke="#1f1f22" stroke-width="2"><circle cx="12" cy="12" r="10"/><ellipse cx="12" cy="12" rx="4.5" ry="10"/><path d="M2 12h20"/></g></svg></span>
          www.kestrelhome.co.uk
        </li>
      </ul>
    </div>
    <p class="address-band">12 Mill Farm Road, Ashbury AB1 2CD</p>
  </section>

</main>
</body>
</html>
```